Building company requiring web site design

We need a web design for a new company based in Sydney called Marlow Building Co. We build and renovate new and existing homes for consumers. We would like to see design that use the colours red and grey. The final design should communicate innovative building but with old fashion quality, great customer service and attention to detail. I have already had a logo and stationary design completed and would like to use the these colour schemes
Updates

Target Market(s)

Home owners, investors

Industry/Entity Type

Building

Coding

Coded - Design and coding required

Number of Pages Required

5+ page

Requirements
Must have
• Home page, contact page, about us page, gallery page and testimonial page
Nice to have
• Contact form

```html
<!DOCTYPE html>
<html lang="en">
<head>
<meta charset="utf-8">
<title>Marlow Building Co. — Building Excellence</title>
<link rel="stylesheet" href="https://fonts.googleapis.com/css2?family=Lato:ital,wght@0,300;0,400;0,700;1,300;1,400&family=Lobster&display=swap">
<style>
:root{
  --red:#b5403f;
  --red-dark:#9c3433;
  --ink:#2b2b2b;
  --charcoal:#2f2f2f;
  --footer:#2a2a2a;
  --bottom:#1c1c1c;
  --text:#6d6d6d;
  --line:#d8d8d8;
  --page:#fafafa;
  --white:#ffffff;
}
*{box-sizing:border-box;margin:0;padding:0}
html,body{width:1200px;height:2946px;overflow:hidden}
body{position:relative;background:var(--page);font-family:'Lato',sans-serif;color:var(--text)}

/* Header */
.site-header{position:absolute;top:0;left:0;width:1200px;height:94px;background:var(--white);border-bottom:1px solid #eee}
.brand{position:absolute;left:157px;top:26px;width:120px;font-size:15px;line-height:19px;font-weight:700;color:var(--ink);letter-spacing:.3px}
.main-nav{position:absolute;left:306px;top:0;height:94px;display:flex;gap:34px;align-items:center}
.main-nav a{font-size:13px;color:var(--ink);text-decoration:none;height:94px;line-height:94px;display:block;white-space:nowrap}
.main-nav a.active{color:var(--red);border-bottom:3px solid var(--red)}
.header-phone{position:absolute;left:915px;top:36px;display:flex;align-items:center;gap:10px;font-size:16px;font-weight:700;color:var(--ink)}

/* Hero */
.hero{position:absolute;top:94px;left:0;width:1200px;height:440px;background:linear-gradient(180deg,#5e6b8e 0%,#8a84a4 30%,#b89a98 55%,#6f4f3f 75%,#2d3324 100%)}
.hero-title{position:absolute;top:112px;width:100%;text-align:center;color:var(--white);font-weight:300;font-size:30px;letter-spacing:1px}
.hero-sub{position:absolute;top:152px;width:100%;text-align:center;color:#f1f1f1;font-size:13px;letter-spacing:8px}
.hero-badge{position:absolute;left:512px;top:446px;width:176px;height:176px;border-radius:50%;background:var(--red);border:5px solid #e9c9c8;box-shadow:0 0 0 3px var(--white);display:flex;align-items:center;justify-content:center;text-align:center;color:var(--white);font-size:19px;font-weight:700;line-height:1.3}

/* Intro */
.intro{position:absolute;top:646px;left:280px;width:640px;text-align:center;font-size:12px;line-height:16px;font-weight:300}

.section-title{position:absolute;left:157px;width:888px;display:flex;align-items:center;gap:26px;color:var(--ink);font-size:23px;font-weight:700}
.section-title::before,.section-title::after{content:"";flex:1;height:1px;background:var(--line)}

/* Services */
.services{position:absolute;top:835px;left:157px;display:flex;gap:25px}
.service-card{width:279px;height:383px;background:var(--white);box-shadow:0 1px 3px rgba(0,0,0,.1)}
.service-card h3{height:49px;background:var(--red);color:var(--white);font-family:'Lobster',cursive;font-weight:400;font-size:19px;padding:12px 16px;letter-spacing:.5px}
.service-media{height:161px}
.service-card p{padding:22px 24px 0 24px;font-size:11.5px;line-height:16px;font-weight:300;height:97px}
.btn{display:inline-block;font-size:11px;color:var(--white);background:var(--ink);padding:8px 16px;text-decoration:none}
.service-card .btn{margin-left:24px}
.btn.red{background:var(--red)}

/* Work grid */
.work-grid{position:absolute;top:1334px;left:0;width:1200px;height:477px;display:grid;grid-template-columns:230px 230px 230px 230px 230px;grid-template-rows:153px 152px 149px;column-gap:12px;row-gap:12px}
.tile.tall{grid-row:span 2}
.tile.feature{grid-row:span 2;background:var(--red);position:relative;display:flex;flex-direction:column;align-items:center;justify-content:center;color:var(--white)}
.feature-name{font-family:'Lobster',cursive;font-size:18px}
.feature-type{font-size:12px;margin-top:2px}
.feature-icon{margin-top:20px}
.view-all{position:absolute;top:1846px;left:536px;width:128px;text-align:center}

/* Testimonials */
.avatar{position:absolute;top:1988px;left:553px;width:94px;height:94px;border-radius:50%;background:linear-gradient(180deg,#c9ccd2,#8b8f97);border:3px solid var(--white);box-shadow:0 1px 4px rgba(0,0,0,.2)}
.quote{position:absolute;top:2096px;left:265px;width:670px;text-align:center;font-size:12px;line-height:16px;font-style:italic;font-weight:300}
.quote-name{position:absolute;top:2186px;width:1200px;text-align:center;font-family:'Lobster',cursive;color:var(--ink);font-size:14px}
.quote-role{position:absolute;top:2206px;width:1200px;text-align:center;font-size:11px}
.arrow{position:absolute;top:2082px}
.skyline{position:absolute;top:2238px;left:430px;width:340px;height:133px;background:linear-gradient(180deg,rgba(0,0,0,0) 0%,#ececec 100%)}

/* CTA */
.cta{position:absolute;top:2371px;left:0;width:1200px;height:110px;background:var(--charcoal)}
.cta-red{position:absolute;left:0;top:0}
.cta-text{position:absolute;left:157px;top:36px;color:var(--white)}
.cta-text h2{font-size:18px;font-weight:400}
.cta-text p{font-size:12px;font-weight:300;margin-top:2px}
.cta-start{position:absolute;left:780px;top:43px;width:120px;text-align:center;padding:9px 0;font-size:13px}
.cta-contact{position:absolute;left:925px;top:43px;width:118px;text-align:center;padding:8px 0;font-size:13px;color:var(--white);border:1px solid #bbb;text-decoration:none}

/* Footer */
.site-footer{position:absolute;top:2481px;left:0;width:1200px;height:402px;background:linear-gradient(180deg,#2b2b2b,#242424)}
.footer-info{position:absolute;left:196px;top:84px;color:#d7d7d7;font-size:11px;line-height:16px;width:226px}
.footer-info h4{color:var(--white);font-size:13px;font-weight:700;padding-bottom:12px;border-bottom:1px solid #555;margin-bottom:18px}
.footer-info h5{color:var(--white);font-size:11px;font-weight:700;margin-top:14px}
.footer-call{color:var(--red);font-size:17px;font-weight:300;margin-top:4px}
.footer-email{color:var(--red);font-size:11px;text-decoration:underline}
.social{display:flex;gap:5px;margin-top:8px}
.social span{width:15px;height:15px;background:#7a7a7a}
.form-frame{position:absolute;left:536px;top:53px;width:1px;height:304px;background:#555}
.form-frame::before,.form-frame::after{content:"";position:absolute;left:0;width:60px;height:1px;background:#555}
.form-frame::before{top:0}.form-frame::after{bottom:0}
.contact-form label{position:absolute;color:#e5e5e5;font-size:11px}
.field{position:absolute;border:1px solid #7a7a7a;background:rgba(255,255,255,.03)}
.form-note{position:absolute;left:611px;top:2746px;color:#cfcfcf;font-size:11px}
.form-note em{color:var(--white);text-decoration:underline}
.send{position:absolute;left:611px;top:2775px;width:108px;height:28px;border:1px solid #aaa;color:var(--white);font-size:11px;display:flex;align-items:center;justify-content:center;gap:8px}

.bottom-bar{position:absolute;top:2883px;left:0;width:1200px;height:63px;background:var(--bottom);color:#9a9a9a;font-size:11px}
.copyright{position:absolute;left:157px;top:25px}
.legal{position:absolute;left:536px;top:25px}
.to-top{position:absolute;left:997px;top:16px;width:32px;height:32px;border-radius:50%;background:var(--red);display:flex;align-items:center;justify-content:center}
</style>
</head>
<body>

<header class="site-header">
  <div class="brand">Marlow<br>Building Co.</div>
  <nav class="main-nav">
    <a href="#">Marlow Building Co.</a>
    <a href="#" class="active">Built New &amp; Existing Home</a>
    <a href="#">Renovation</a>
    <a href="#">Our work</a>
    <a href="#">Contact Us</a>
  </nav>
  <div class="header-phone">
    <svg width="16" height="18" viewBox="0 0 16 18"><rect x="2" y="1" width="12" height="16" rx="2" fill="none" stroke="#b5403f" stroke-width="2"/><rect x="6" y="13" width="4" height="2" fill="#b5403f"/></svg>
    0400 555 018
  </div>
</header>

<section class="hero" role="img" aria-label="Modern timber and glass home with pavilion at dusk">
  <h1 class="hero-title">BUILDING EXCELLENCE</h1>
  <p class="hero-sub">Marlow Building &amp; Renovations</p>
</section>
<div class="hero-badge">Marlow<br>Building Co.</div>

<p class="intro">Our company based in Sydney called Marlow Building Co. We build and renovate new and existing homes for consumers. Lorem Ipsum is simply dummy text of the printing and typesetting industry. Lorem Ipsum has been the industry's standard dummy text ever since the 1500s, when an unknown printer took a galley of type and scrambled it to make a type specimen book. It has survived not only five centuries, but also the leap into electronic typesetting, remaining essentially unchanged.</p>

<h2 class="section-title" style="top:762px">What We Do ?</h2>

<div class="services">
  <article class="service-card">
    <h3>Repairs</h3>
    <div class="service-media" role="img" aria-label="Carpenter measuring timber framing" style="background:linear-gradient(135deg,#e9d7b4,#a77a45 60%,#5a3b22)"></div>
    <p>If you've looking to build a house, we can help you achieve your dream. Marlow Building Co. have completed many new home builds for both families and individuals across the region.</p>
    <a href="#" class="btn red">Read More</a>
  </article>
  <article class="service-card">
    <h3>Renovations</h3>
    <div class="service-media" role="img" aria-label="House under construction with timber frame" style="background:linear-gradient(180deg,#bcd3ea 0%,#c8b08c 55%,#8d7256)"></div>
    <p>If you've looking to build a house, we can help you achieve your dream. Marlow Building Co. have completed many new home builds for both families and individuals across the region.</p>
    <a href="#" class="btn">Read More</a>
  </article>
  <article class="service-card">
    <h3>Construction</h3>
    <div class="service-media" role="img" aria-label="Builder reviewing plans with a couple on site" style="background:linear-gradient(135deg,#d9c9a5,#b49566 50%,#4d6f9a)"></div>
    <p>If you've looking to build a house, we can help you achieve your dream. Marlow Building Co. have completed many new home builds for both families and individuals across the region.</p>
    <a href="#" class="btn">Read More</a>
  </article>
</div>

<h2 class="section-title" style="top:1276px">Our Work</h2>

<div class="work-grid">
  <div class="tile" role="img" aria-label="Two-storey family home with lawn" style="background:linear-gradient(180deg,#9fc0e0,#c9b9a0 55%,#6e8a4a)"></div>
  <div class="tile tall" role="img" aria-label="Bright white kitchen with marble bench" style="background:linear-gradient(160deg,#f4f4f4,#d9dcdf 60%,#b9bcc0)"></div>
  <div class="tile" role="img" aria-label="Living room with leather sofas" style="background:linear-gradient(180deg,#f0e2c8,#b48a5c 60%,#6b3b25)"></div>
  <div class="tile tall" role="img" aria-label="Brick home under blue sky" style="background:linear-gradient(180deg,#3f6fb0,#8aa9cf 40%,#a88a72 70%,#5f7c3d)"></div>
  <div class="tile" role="img" aria-label="Large white coastal house" style="background:linear-gradient(180deg,#4b7fc0,#e7e4dc 55%,#6f9a4c)"></div>
  <div class="tile" role="img" aria-label="Living room with leather sofas" style="background:linear-gradient(180deg,#f0e2c8,#b48a5c 60%,#6b3b25)"></div>
  <div class="tile feature">
    <div class="feature-name">Ashcombe</div>
    <div class="feature-type">Present New Build</div>
    <svg class="feature-icon" width="14" height="14" viewBox="0 0 14 14" fill="none" stroke="#fff" stroke-width="1.5"><path d="M8 1h5v5M13 1 8 6M6 13H1V8M1 13l5-5"/></svg>
  </div>
  <div class="tile" role="img" aria-label="Living room with leather sofas" style="background:linear-gradient(180deg,#f0e2c8,#b48a5c 60%,#6b3b25)"></div>
  <div class="tile" role="img" aria-label="Two-storey family home with lawn" style="background:linear-gradient(180deg,#9fc0e0,#c9b9a0 55%,#6e8a4a)"></div>
  <div class="tile" role="img" aria-label="Large white coastal house" style="background:linear-gradient(180deg,#4b7fc0,#e7e4dc 55%,#6f9a4c)"></div>
  <div class="tile" role="img" aria-label="Bright white kitchen with marble bench" style="background:linear-gradient(160deg,#f4f4f4,#d9dcdf 60%,#b9bcc0)"></div>
  <div class="tile" role="img" aria-label="Two-storey family home with lawn" style="background:linear-gradient(180deg,#9fc0e0,#c9b9a0 55%,#6e8a4a)"></div>
</div>

<a href="#" class="btn view-all">View All Work</a>

<h2 class="section-title" style="top:1932px">Testimonials</h2>

<div class="avatar" role="img" aria-label="Client portrait"></div>
<svg class="arrow" style="left:166px" width="22" height="40" viewBox="0 0 22 40"><path d="M20 2 3 20l17 18" fill="none" stroke="#bbb" stroke-width="2"/></svg>
<svg class="arrow" style="left:1000px" width="22" height="40" viewBox="0 0 22 40"><path d="M2 2l17 18L2 38" fill="none" stroke="#b5403f" stroke-width="2"/></svg>
<p class="quote">Lorem Ipsum is simply dummy text of the printing and typesetting industry. Lorem Ipsum has been the industry's standard dummy text ever since the 1500s, when an unknown printer took a galley of type and scrambled it to make a type specimen book. It has survived not only five centuries, but also the leap into electronic typesetting, remaining essentially unchanged.</p>
<p class="quote-name">Corey Lawton</p>
<p class="quote-role">- Project Manager at Harbourline -</p>
<div class="skyline" role="img" aria-label="Faint city skyline decoration"></div>

<section class="cta">
  <svg class="cta-red" width="728" height="110" viewBox="0 0 728 110"><polygon points="0,0 728,0 655,110 0,110" fill="#b5403f"/></svg>
  <div class="cta-text">
    <h2>Lets start making plans to build your dreams</h2>
    <p>Our expert builders will transform your home</p>
  </div>
  <a href="#" class="btn red cta-start">Get Started</a>
  <a href="#" class="cta-contact">Contact Us</a>
</section>

<footer class="site-footer">
  <div class="footer-info">
    <h4>Drop Us a Message!</h4>
    <p>Marlow Building Co.<br>42 Mill Lane, Newtown<br>Parkside SA 5000</p>
    <h5>Contact Info</h5>
    <p class="footer-call">Call: 0400 555 018</p>
    <p class="footer-email">hello@marlowbuilding.com.au</p>
    <h5 style="margin-top:22px">Get Social</h5>
    <div class="social" aria-label="Social links"><span></span><span></span><span></span><span></span><span></span></div>
  </div>
  <div class="form-frame"></div>
</footer>

<form class="contact-form">
  <label style="left:611px;top:2560px">Name</label>
  <div class="field" style="left:611px;top:2579px;width:204px;height:31px"></div>
  <label style="left:839px;top:2560px">Email</label>
  <div class="field" style="left:839px;top:2579px;width:204px;height:31px"></div>
  <label style="left:611px;top:2625px">Message</label>
  <div class="field" style="left:611px;top:2644px;width:432px;height:82px"></div>
</form>
<p class="form-note">If you need to add attachments to the message please <em>Click Here »</em></p>
<div class="send">
  <svg width="12" height="12" viewBox="0 0 12 12"><path d="M1 6 11 1 8 11 6 7Z" fill="none" stroke="#fff" stroke-width="1.2"/></svg>
  Send
</div>

<div class="bottom-bar">
  <span class="copyright">Copyright 2016 © Marlow Building Co.</span>
  <span class="legal">Copyright | Privacy &amp; Cookies Policy | Terms &amp; Conditions</span>
  <div class="to-top"><svg width="12" height="10" viewBox="0 0 12 10"><path d="M1 8 6 2l5 6" fill="none" stroke="#fff" stroke-width="2"/></svg></div>
</div>

</body>
</html>
```